Book cover design for a book named BLOOM

Hello Designers,
The name of the book is BLOOM and it is about unexpected experiences individuals have which are beyond their control. Occurrences they are unable to overcome or get out of themselves without the help of God. After overcoming these situations they know only God could have done this for them, no one else could have. It is an adult Christian book. I would like you to be as creative as you can with the cover, using color, light, graphic designs, shapes, scale, lines etc. (you are the designers, I don't know how to do these things.) I would like to use the image created on a paperback, hardcover or e book. I tried to use an image from Pixmarble just to give you some idea of my thinking but you do not have to use these hands. The hands should look as if they are giving someone the word TESTIMONY not receiving it. Use of the words provided, the light rays, and some type of hands extended should not change, but how you use them is up to you. Use the words, light rays, and hands however you wish as long as they convey someone giving the word TESTIMONY. The word TESTIMONY should be proportional to the hand in size and should appear as if being held in the actual hand it should not be larger than the book name. It is a Christian book of testimonies. Also for your design samples you can use the name Marlene Quiller for the author. Thank you, please feel free to contact me if you have any questions. I am looking for the cover to be an attention grabber and give the reader something to really think about and remember visually when they see this cover. Thank you again.

Target Market(s)

anyone and christians

Requirements
Must have
• Use of the words provided, the light rays, and some type of hands extended should not change.
Nice to have
• be as creative as you can with the cover, using color, light, graphic designs, shapes, scale, lines etc. (you are the designers, I don't know how to do these things.)
Should not have
• It should not have fonts, colors, etc. that convey it is a child's book, fairytale, or fictional etc. It is a book of true stories that actually happened. It should not look exactly like my example, what I provided.

```html
<!DOCTYPE html>
<html lang="en">
<head>
<meta charset="utf-8">
<title>BLOOM – Book Cover Wrap</title>
<link rel="stylesheet" href="https://fonts.googleapis.com/css2?family=Cinzel:wght@400;600&family=Open+Sans:wght@400;700&family=Arimo:wght@700&family=Anton&display=swap">
<style>
  :root {
    --paper: #ffffff;
    --ink: #000000;
    --type-light: #f2f2f2;
    --type-dark: #1b1510;
    --silver-hi: #ffffff;
    --silver-mid: #b9b9b9;
    --silver-lo: #6d6d6d;
    --copper-hi: #ffe2b8;
    --copper-mid: #c77a34;
    --copper-lo: #5a2f12;
    --barcode-box: #ececec;
    --barcode-text: #444444;
    --glow: #fffdf5;
    --skin-light: #d9b08c;
    --skin-dark: #7a5236;
  }
  * { box-sizing: border-box; margin: 0; padding: 0; }
  html, body { width: 1200px; height: 881px; overflow: hidden; background: var(--paper); }
  .canvas { position: relative; width: 1200px; height: 881px; background: var(--paper); }
  .wrap { position: absolute; left: 12px; top: 12px; width: 1176px; height: 857px; background: var(--ink); overflow: hidden; }

  /* Back cover */
  .back-headline {
    position: absolute; left: 40px; width: 510px; top: 66px; text-align: center;
    font-family: "Cinzel", serif; font-weight: 400; font-size: 21px; line-height: 30px; color: var(--type-light);
  }
  .back-body {
    position: absolute; left: 47px; top: 166px; width: 492px;
    font-family: "Open Sans", sans-serif; font-size: 11.6px; line-height: 18.5px; color: var(--type-light);
  }
  .back-body p + p { margin-top: 18.5px; }
  .author-photo { position: absolute; left: 47px; top: 570px; width: 92px; height: 114px; background: var(--paper); }
  .about-title {
    position: absolute; left: 166px; width: 340px; top: 567px; text-align: center;
    font-family: "Open Sans", sans-serif; font-weight: 400; font-size: 11.5px; color: var(--type-light);
  }
  .about-body {
    position: absolute; left: 166px; top: 590px; width: 360px;
    font-family: "Open Sans", sans-serif; font-size: 8.7px; line-height: 14.4px; color: var(--type-light);
  }
  .barcode-slot {
    position: absolute; left: 357px; top: 718px; width: 190px; height: 112px; background: var(--barcode-box);
    display: flex; align-items: center; justify-content: center; text-align: center;
    font-family: "Open Sans", sans-serif; font-weight: 700; font-size: 15.5px; line-height: 24px; color: var(--barcode-text);
  }

  /* Spine */
  .spine { position: absolute; left: 566px; top: 0; width: 44px; height: 857px; }
  .spine-text { position: absolute; left: 50%; transform-origin: 0 0; transform: rotate(90deg); white-space: nowrap; color: var(--type-light); }
  .spine-tagline { top: 60px; font-family: "Cinzel", serif; font-size: 9.5px; line-height: 12px; margin-left: 13px; }
  .spine-title {
    top: 356px; margin-left: 26px; font-family: "Cinzel", serif; font-weight: 600; font-size: 46px; line-height: 50px;
    background: linear-gradient(180deg, var(--silver-hi), var(--silver-mid) 55%, var(--silver-lo));
    -webkit-background-clip: text; background-clip: text; color: transparent;
  }
  .spine-author { top: 622px; margin-left: 11px; font-family: "Cinzel", serif; font-size: 18px; letter-spacing: 3px; line-height: 22px; }

  /* Front cover */
  .front { position: absolute; left: 612px; top: 0; width: 564px; height: 857px; }
  .hands-light {
    position: absolute; inset: 0;
    background:
      radial-gradient(ellipse 230px 120px at 285px 505px, rgba(255,250,238,0.95) 0%, rgba(250,236,214,0.85) 55%, transparent 100%),
      radial-gradient(ellipse 160px 190px at 285px 420px, var(--glow) 0%, rgba(255,253,245,0.9) 40%, rgba(255,240,210,0.3) 75%, transparent 100%),
      radial-gradient(ellipse 280px 320px at 285px 420px, rgba(255,255,255,0.3), transparent 75%),
      radial-gradient(ellipse 300px 240px at 285px 790px, var(--skin-light) 0%, var(--skin-dark) 55%, transparent 88%),
      var(--ink);
  }
  .front-title {
    position: absolute; left: 0; width: 564px; top: 58px; text-align: center;
    font-family: "Cinzel", serif; font-weight: 600; font-size: 128px; line-height: 140px; letter-spacing: -4px;
    background: linear-gradient(180deg, var(--silver-hi) 10%, var(--silver-mid) 50%, var(--silver-lo) 62%, var(--silver-hi) 90%);
    -webkit-background-clip: text; background-clip: text; color: transparent;
  }
  .front-tagline {
    position: absolute; left: 0; width: 564px; top: 207px; text-align: center;
    font-family: "Cinzel", serif; font-weight: 400; font-size: 21.5px; line-height: 31px; color: var(--type-light);
  }
  .promise {
    position: absolute; left: 0; width: 564px; top: 500px; text-align: center;
    font-family: "Arimo", sans-serif; font-weight: 700; font-size: 23px; letter-spacing: -0.5px; color: var(--type-dark);
  }
  .testimony {
    position: absolute; left: 0; width: 564px; top: 528px; text-align: center;
    font-family: "Anton", sans-serif; font-size: 74px; line-height: 86px; letter-spacing: 2px;
    background: linear-gradient(180deg, var(--copper-hi) 8%, var(--copper-mid) 45%, var(--copper-lo) 60%, var(--copper-mid) 85%);
    -webkit-background-clip: text; background-clip: text; color: transparent;
  }
  .front-author {
    position: absolute; left: 0; width: 564px; top: 786px; text-align: center;
    font-family: "Cinzel", serif; font-size: 30px; letter-spacing: 4px; color: var(--type-light);
  }
</style>
</head>
<body>
<div class="canvas">
  <div class="wrap">
    <section class="back-cover">
      <h2 class="back-headline">BEFORE THERE WILL EVER BE A TESTIMONY<br>THERE MUST ALWAYS BE AN EXPERIENCE</h2>
      <div class="back-body">
        <p>The name of the book is BLOOM and it is about unexpected experiences individuals have which are beyond their control. Occurrences they are unable to overcome or get out of themselves without the help of God.<br>After overcoming these situations they know only God could have done this for them, no one else could have. It is an adult Christian book. I would like you to be as creative as you can with the cover, using color, light, graphic designs, shapes, scale, lines etc. (you are the designers, I don't know how to do these things.) I would like to use the image created on a paperback, hardcover or e book. I tried to use an image from Pixmarble just to give you some idea of my thinking but you do not have to use these hands.</p>
        <p>The hands should look as if they are giving someone the word TESTIMONY not receiving it. Use of the words provided, the light rays, and some type of hands extended should not change, but how you use them is up to you. Use the words, light rays, and hands however you wish as long as they convey someone giving the word TESTIMONY. The word TESTIMONY should be proportional to the hand in size and should appear as if being held in the actual hand it should not be larger than the book name.<br>It is a Christian book of testimonies. Also for your design samples you can use the name Marlene Quiller for the author. Thank you, please feel free to contact me if you have any questions. I am looking for the cover to be an attention grabber and give the reader something to really think about and remember visually when they see this cover.</p>
      </div>
      <div class="author-photo" role="img" aria-label="Author photo placeholder"></div>
      <h3 class="about-title">About the Author:</h3>
      <p class="about-body">It is a Christian book of testimonies. Also for your design samples you can use the name Marlene Quiller for the author. Thank you, please feel free to contact me if you have any questions. I am looking for the cover to be an attention grabber and give the reader something to really think about and remember visually when they see this cover.</p>
      <div class="barcode-slot">Barcode<br>Location &amp; Size<br>2” X 1.2”</div>
    </section>

    <section class="spine">
      <div class="spine-text spine-tagline">BEFORE THERE WILL EVER BE A TESTIMONY<br>THERE MUST ALWAYS BE AN EXPERIENCE</div>
      <div class="spine-text spine-title">BLOOM</div>
      <div class="spine-text spine-author">MARLENE QUILLER</div>
    </section>

    <section class="front">
      <div class="hands-light" role="img" aria-label="Photograph of two open cupped hands extended upward with bright white light rays bursting from them"></div>
      <h1 class="front-title">BLOOM</h1>
      <p class="front-tagline">BEFORE THERE WILL EVER BE A TESTIMONY<br>THERE MUST ALWAYS BE AN EXPERIENCE</p>
      <p class="promise">OUT OF THE TEST I’VE GIVEN YOU A</p>
      <p class="testimony">TESTIMONY</p>
      <p class="front-author">MARLENE QUILLER</p>
    </section>
  </div>
</div>
</body>
</html>
```